Need a business card created for my Heating and Air-conditioning business

We are a new Air Conditioning , Refrigeration and Heating business called Frost & Cinder HVAC/R - we do repairs, maintenance and installations.

Our motto is "Skilled Precision - Superior Value"

Information needed on the card:
Leon Marsh
604-555-0187
www.frosthvac.example
info@frosthvac.example

```html
<!DOCTYPE html>
<html lang="en">
<head>
<meta charset="utf-8">
<title>Frost &amp; Cinder HVAC/R – Business Card</title>
<link rel="stylesheet" href="https://fonts.googleapis.com/css2?family=Oswald:wght@300;400;700&family=Montserrat:wght@300;400;700&family=Cormorant+Garamond:wght@500&display=swap">
<style>
  :root {
    --backdrop: #9a9a9a;
    --card-dark: #1c1c1c;
    --card-dark-deco: #2a2a2a;
    --card-light: #ffffff;
    --deco-light: #f1f1f1;
    --ink: #111111;
    --ink-soft: #8a8a8a;
    --white: #ffffff;
    --ice: #6cb4ee;
    --ember: #e0202f;
    --gas: #f0a12a;
    --power: #2bd36b;
    --air: #c4c4c4;
    --indoor: #f2d319;
  }
  * { box-sizing: border-box; margin: 0; padding: 0; }
  html, body { width: 1200px; height: 1000px; overflow: hidden; }
  body { background: var(--backdrop); position: relative; font-family: "Montserrat", sans-serif; }

  .card {
    position: absolute;
    left: 210px;
    width: 780px;
    height: 450px;
    border-radius: 30px;
    overflow: hidden;
  }
  .card--front { top: 30px; background: var(--card-dark); }
  .card--back { top: 520px; background: var(--card-light); }

  .deco-area { position: absolute; top: 0; right: 0; width: 330px; height: 450px; }
  .card--front .deco-area {
    background: radial-gradient(ellipse at 70% 65%, var(--card-dark-deco) 0%, var(--card-dark) 70%);
  }
  .card--back .deco-area {
    background: radial-gradient(ellipse at 70% 60%, var(--deco-light) 0%, var(--card-light) 72%);
  }

  .brand {
    position: absolute;
    left: 195px;
    top: 131px;
    display: flex;
    align-items: center;
    gap: 22px;
    color: var(--white);
    font-family: "Cormorant Garamond", serif;
    font-weight: 500;
  }
  .brand__mark {
    width: 150px; height: 150px;
    border: 2px solid var(--white);
    border-radius: 50%;
    flex: none;
  }
  .brand__name { font-size: 44px; letter-spacing: 4px; line-height: 1.1; }
  .brand__tag { font-size: 22px; letter-spacing: 2px; margin-top: 8px; }

  .person {
    position: absolute;
    left: 150px;
    top: 200px;
    width: 220px;
    text-align: right;
  }
  .person__name {
    font-family: "Oswald", sans-serif;
    font-size: 38px;
    line-height: 1;
    color: var(--ink);
    letter-spacing: 1px;
  }
  .person__first { font-weight: 300; }
  .person__last { font-weight: 700; }
  .person__role {
    font-family: "Montserrat", sans-serif;
    font-weight: 700;
    font-size: 12px;
    letter-spacing: 3px;
    margin-top: 6px;
    color: var(--ink);
  }
  .divider {
    position: absolute;
    left: 389px; top: 192px;
    width: 1px; height: 80px;
    background: var(--ink-soft);
  }
  .contacts { position: absolute; left: 410px; top: 189px; list-style: none; }
  .contacts li {
    display: flex; align-items: center; gap: 14px;
    height: 27px;
    font-size: 21px; font-weight: 300;
    color: var(--ink-soft);
  }
  .contacts svg { width: 16px; height: 16px; flex: none; }

  .services { position: absolute; left: 0; top: 340px; width: 100%; height: 90px; list-style: none; }
  .service {
    position: absolute;
    width: 120px;
    margin-left: -60px;
    text-align: center;
  }
  .service svg { width: 56px; height: 56px; display: block; margin: 0 auto; }
  .service__label {
    display: block;
    margin-top: 14px;
    font-family: "Oswald", sans-serif;
    font-weight: 400;
    font-size: 12px;
    letter-spacing: 2px;
    color: var(--ink);
  }
</style>
</head>
<body>

<section class="card card--front" aria-label="Card front">
  <div class="deco-area" role="img" aria-label="Large dark silhouette illustration of a bear breathing swirling air"></div>
  <div class="brand">
    <span class="brand__mark"></span>
    <div>
      <div class="brand__name">Frost &amp; Cinder</div>
      <div class="brand__tag">HVAC/R</div>
    </div>
  </div>
</section>

<section class="card card--back" aria-label="Card back">
  <div class="deco-area" role="img" aria-label="Faint line illustration of a bear breathing swirling air"></div>

  <div class="person">
    <div class="person__name"><span class="person__first">LEON</span> <span class="person__last">MARSH</span></div>
    <div class="person__role">OWNER</div>
  </div>
  <div class="divider"></div>

  <ul class="contacts">
    <li>
      <svg viewBox="0 0 16 16"><path d="M4 1 L6.5 1 L7.5 5 L5.5 6.5 C6.5 8.5 7.5 9.5 9.5 10.5 L11 8.5 L15 9.5 L15 12 C15 13.5 14 15 12 15 C6 14.5 1.5 10 1 4 C1 2 2.5 1 4 1 Z" fill="#111"/></svg>
      604-555-0187
    </li>
    <li>
      <svg viewBox="0 0 16 16"><rect x="1" y="3" width="14" height="10" fill="#111"/><path d="M1 3 L8 9 L15 3 M1 13 L6 8 M15 13 L10 8" stroke="#fff" stroke-width="1.2" fill="none"/></svg>
      www.frosthvac.example
    </li>
    <li>
      <svg viewBox="0 0 16 16"><circle cx="8" cy="8" r="7" fill="#111"/><path d="M1 8 H15 M8 1 V15 M3 4.5 H13 M3 11.5 H13" stroke="#fff" stroke-width="0.9" fill="none"/><ellipse cx="8" cy="8" rx="3" ry="7" stroke="#fff" stroke-width="0.9" fill="none"/></svg>
      info@frosthvac.example
    </li>
  </ul>

  <ul class="services">
    <li class="service" style="left:148px">
      <svg viewBox="0 0 56 56" fill="none" stroke="var(--ice)" stroke-width="1.6" stroke-linecap="round">
        <path d="M28 2 V54 M5.5 15 L50.5 41 M5.5 41 L50.5 15"/>
        <path d="M23 7 L28 12 L33 7 M23 49 L28 44 L33 49 M7 22 L14 19 L11 12 M49 34 L42 37 L45 44 M7 34 L14 37 L11 44 M49 22 L42 19 L45 12"/>
      </svg>
      <span class="service__label">REFRIGERATION</span>
    </li>
    <li class="service" style="left:268px">
      <svg viewBox="0 0 56 56" fill="none" stroke="var(--ember)" stroke-width="1.6">
        <circle cx="28" cy="28" r="26"/><circle cx="28" cy="28" r="21"/>
        <circle cx="28" cy="28" r="3"/>
        <path d="M28 25 C22 18 24 11 31 12 C36 14 32 21 28 25 Z M31 28 C38 22 45 24 44 31 C42 36 35 32 31 28 Z M28 31 C34 38 32 45 25 44 C20 42 24 35 28 31 Z M25 28 C18 34 11 32 12 25 C14 20 21 24 25 28 Z"/>
      </svg>
      <span class="service__label">HEAT PUMPS</span>
    </li>
    <li class="service" style="left:357px">
      <svg viewBox="0 0 56 56"><path d="M28 4 C32 14 42 22 42 36 C42 46 35 52 28 52 C21 52 14 46 14 37 C14 29 19 25 21 19 C24 24 24 28 26 30 C29 22 30 13 28 4 Z" fill="var(--gas)"/><path d="M28 30 C31 36 35 40 34 45 C33 49 30 50 28 50 C25 50 22 48 22 44 C22 40 26 36 28 30 Z" fill="#fff"/></svg>
      <span class="service__label">GAS</span>
    </li>
    <li class="service" style="left:443px">
      <svg viewBox="0 0 56 56" fill="none" stroke="var(--power)" stroke-width="2" stroke-linejoin="round">
        <circle cx="28" cy="28" r="23"/>
        <path d="M31 12 L20 31 H28 L25 44 L36 25 H28 Z"/>
      </svg>
      <span class="service__label">ELECTRICAL</span>
    </li>
    <li class="service" style="left:548px">
      <svg viewBox="0 0 56 56" fill="none" stroke="var(--air)" stroke-width="2.2" stroke-linecap="round">
        <path d="M4 22 H34 C39 22 40 14 35 14 C32 14 31 17 32 18"/>
        <path d="M4 30 H44 C50 30 50 22 45 22"/>
        <path d="M8 38 H36 C42 38 42 46 37 46 C34 46 33 43 34 42"/>
      </svg>
      <span class="service__label">VENTILATION</span>
    </li>
    <li class="service" style="left:649px">
      <svg viewBox="0 0 56 56" fill="none" stroke="var(--indoor)" stroke-width="1.6" stroke-linecap="round">
        <circle cx="28" cy="28" r="26"/>
        <circle cx="28" cy="28" r="12"/>
        <path d="M28 16 V9 M28 40 V47 M16 28 H9 M40 28 H47 M19.5 19.5 L14.5 14.5 M36.5 36.5 L41.5 41.5 M36.5 19.5 L41.5 14.5 M19.5 36.5 L14.5 41.5"/>
        <path d="M25 9 H31 M25 47 H31 M9 25 V31 M47 25 V31"/>
        <circle cx="24" cy="25" r="2"/><circle cx="32" cy="25" r="2"/><circle cx="28" cy="32" r="2"/>
      </svg>
      <span class="service__label">INDOOR AIR</span>
    </li>
  </ul>
</section>

</body>
</html>
```